Business Card Design

I am a criminologist running a research and consultancy business on my own (PKConsultants)
I specialise in looking at fraud and other white-collar crimes. Also governance issues..
I would like a professional business card that would be appropriate both in the academic and business sector as I straddle both sectors. Normal shape - not square.
I am interested in seeing border Word Cloud type projects - black on white or white on black..
Example key words would be fraud, research, qualitative, interviews, quantitative, white-collar, reports, government, surveys, sample, governance, assurance, crime, offenders, prison etc (I can provide a full list if this is the option I go for). I also like Word Cloud borders as attached.
I am also interested in seeing other style business cards. Preferably one colour, plus black and white.
In particular I like black backgrounds with coloured words etc - colours like lime green are good.
I also like blues - especially teal if a traditional white background is chosen.
I don't have a logo - unless anyone can think of anything that's particularly appropriate.
Graphics can be used but they would be simple and stylish (dots, squares, lines, curves etc)
I would like the design to translate simply for a header for a website or blog.
My current website is www.pelling-hurst.com but is out of date in terms of what I do and design.
I have attached a number of things that have caught my eye and inspired me.
I have asked for a one-sided business card in the first instance - however if someone comes up with a good cloud design that might go on one side, I would consider a two-sided one.
Design can be landscape or portrait.
Kind Regards
Meg
Landscape
Contact Information for Business Card
PKConsultants
Dr Margery Pelling-Hurst, MSc, BSc, **
42 Brindle Wold
Harlow Cross, Wendmoor
KX27 4QD
+44(0)1620 482917
+44(0)7531 804152
www.pelling-hurst.com
margery@pelling-hurst.com

```html
<!DOCTYPE html>
<html lang="en">
<head>
<meta charset="utf-8">
<title>PKConsultants — Business Card</title>
<link href="https://fonts.googleapis.com/css2?family=Montserrat:wght@400;500;600&display=swap" rel="stylesheet">
<style>
  :root {
    --page: #efefef;
    --card: #050505;
    --lime: #5fc93f;
    --lime-soft: #4fae33;
    --texture-light: #161616;
    --texture-dark: #070707;
  }
  * { margin: 0; padding: 0; box-sizing: border-box; }
  html, body {
    width: 1200px; height: 800px; overflow: hidden;
    background: var(--page);
  }
  .canvas {
    position: relative; width: 1200px; height: 800px;
    display: flex; align-items: center; justify-content: center;
  }
  .card {
    position: relative; width: 910px; height: 560px;
    background: var(--card); overflow: hidden;
    box-shadow: 0 14px 30px rgba(0,0,0,.18);
    font-family: "Montserrat", sans-serif;
    color: var(--lime);
  }
  .keyword-texture {
    position: absolute; left: 240px; top: 0; right: 0; bottom: 0;
    background: radial-gradient(ellipse at 55% 50%, var(--texture-light) 0%, var(--texture-dark) 75%);
  }
  .brand {
    position: absolute; left: 60px; top: 50px;
    display: flex; align-items: center; gap: 22px;
  }
  .brand-square { width: 150px; height: 110px; background: var(--lime); }
  .brand-name {
    font-weight: 600; font-size: 30px; letter-spacing: 1px; color: var(--lime);
  }
  .quick-contact {
    position: absolute; left: 62px; top: 182px;
    font-size: 15px; line-height: 1.55; letter-spacing: 1.5px; color: var(--lime-soft);
  }
  .details {
    position: absolute; left: 62px; bottom: 60px;
    letter-spacing: 2px;
  }
  .person-name { font-size: 27px; font-weight: 500; margin-bottom: 18px; }
  .address, .online { font-size: 18px; line-height: 1.6; font-weight: 400; }
</style>
</head>
<body>
<div class="canvas">
  <section class="card" aria-label="PKConsultants business card">
    <div class="keyword-texture" role="img" aria-label="Faint background cloud of research keywords such as fraud, governance and research"></div>

    <div class="brand">
      <div class="brand-square"></div>
      <span class="brand-name">PKConsultants</span>
    </div>

    <div class="quick-contact">
      <p>Dr Margery Pelling-Hurst</p>
      <p>+44(0)1620 482917</p>
      <p>+44(0)7531 804152</p>
      <p>www.pelling-hurst.com</p>
    </div>

    <div class="details">
      <p class="person-name">Dr Margery Pelling-Hurst, MSc, BSc</p>
      <p class="address">42 Brindle Wold Harlow Cross, Wendmoor KX27 4QD</p>
      <p class="online">www.pelling-hurst.com margery@pelling-hurst.com</p>
    </div>
  </section>
</div>
</body>
</html>
```